The Copper Hour ebook cover for Desmond Okafor Whitley

I need an ebook cover/jpeg that depicts a Middle-Eastern desert and sky. The cover must be very elegant and very austere, the simpler the better.
Toward the top, the text will read: The Copper Hour
Directly below the title will read: Corvin Teague
The dimensions for the cover should be 2560 pixels (height) and 1600 pixels (width.)

Target Market(s)

Readers of serious magical realism and/or fantasy literature with a serious literary element.

Font styles to use
Serif

Requirements
Must have
• My ebook cover MUST be a painting or illustration depicting a very austere Middle-Eastern desert and desert sky. Must be elegant and austere. The lettering of the title and author name must blend in beautifully with the image--just like fine books in a bookstore. Title must appear at the top: The Copper Hour. The author's name must appear below title and read: Corvin Teague. Dimensions must be 2560 pixels (height) by 1600 pixels (width)
Nice to have
• A very austere desert on the bottom and a sad elegant sky above.
Should not have
• My ebook cover should not have a spine or a back. I just need an ebook cover of the dimensions stated above.

```html
<!DOCTYPE html>
<html lang="en">
<head>
<meta charset="utf-8">
<title>The Copper Hour — Ebook Cover</title>
<link href="https://fonts.googleapis.com/css2?family=Pinyon+Script&family=Playfair+Display:wght@500&family=Cormorant+Garamond:wght@500&display=swap" rel="stylesheet">
<style>
  :root {
    --backdrop: #2a2a2a;
    --sky-top: #4f3b58;
    --sky-mid: #9a4f6a;
    --sky-glow: #d9606a;
    --haze: #c2574f;
    --dune-crest: #e0824c;
    --dune-mid: #c85a32;
    --dune-base: #a8402a;
    --ink-cream: #fbf2e2;
  }
  * { margin: 0; padding: 0; box-sizing: border-box; }
  html, body {
    width: 1200px;
    height: 900px;
    overflow: hidden;
    background: var(--backdrop);
  }
  .stage {
    width: 1200px;
    height: 900px;
    display: flex;
    align-items: center;
    justify-content: center;
  }
  .cover {
    position: relative;
    width: 510px;
    height: 816px;
    overflow: hidden;
    box-shadow: 0 6px 18px rgba(0,0,0,0.45);
  }
  .cover-art {
    position: absolute;
    inset: 0;
    background: linear-gradient(
      to bottom,
      var(--sky-top) 0%,
      var(--sky-mid) 18%,
      var(--sky-glow) 34%,
      var(--haze) 41%,
      #8f3e3e 44%,
      var(--dune-crest) 47%,
      var(--dune-mid) 65%,
      var(--dune-base) 100%
    );
  }
  .title-block {
    position: absolute;
    top: 104px;
    left: 0;
    right: 0;
    text-align: center;
    color: var(--ink-cream);
  }
  .title-article {
    display: block;
    font-family: "Pinyon Script", cursive;
    font-size: 40px;
    line-height: 1;
    margin-bottom: -4px;
  }
  .title-main {
    display: block;
    font-family: "Playfair Display", serif;
    font-weight: 500;
    font-size: 58px;
    line-height: 1.02;
    letter-spacing: -0.5px;
  }
  .title-main.large {
    font-size: 78px;
    line-height: 0.95;
  }
  .author {
    position: absolute;
    bottom: 32px;
    left: 0;
    right: 0;
    text-align: center;
    font-family: "Cormorant Garamond", serif;
    font-weight: 500;
    font-size: 30px;
    letter-spacing: 0.5px;
    color: var(--ink-cream);
  }
</style>
</head>
<body>
  <main class="stage">
    <article class="cover">
      <div class="cover-art" role="img" aria-label="Rippled red desert dune beneath a violet and coral dusk sky"></div>
      <h1 class="title-block">
        <span class="title-article">The</span>
        <span class="title-main">COPPER</span>
        <span class="title-main large">HOUR</span>
      </h1>
      <p class="author">CORVIN TEAGUE</p>
    </article>
  </main>
</body>
</html>
```